Clean and modern business cards

Looking for an updated business card design for my dental office “corvanta dental” . Looking for a modern clean / sleek design . I’m thinking black background but open to seeing other options . One side needs to have an appointment card . Card needs to have logo, dentist name , phone, email , address . I’ve attached couple of cards I thought were cool as well as my logo
Target Market(s)
Dental patients
Industry/Entity Type
Dentistry
Contact Information for Business Card
Phone email address

```html
<!DOCTYPE html>
<html lang="en">
<head>
<meta charset="utf-8">
<title>Corvanta Dental – Appointment Cards</title>
<link href="https://fonts.googleapis.com/css2?family=Poppins:wght@400;500;600&display=swap" rel="stylesheet">
<style>
  :root {
    --page: #ffffff;
    --card: #231f20;
    --gold: #f9b84c;
    --field: #636266;
  }
  * { margin: 0; padding: 0; box-sizing: border-box; }
  html, body { width: 1200px; height: 1200px; overflow: hidden; background: var(--page); }
  body { position: relative; font-family: "Poppins", sans-serif; color: var(--gold); }

  .appointment-card {
    position: absolute;
    left: 133px;
    width: 941px;
    height: 553px;
    background: var(--card);
    border-radius: 64px;
  }
  .appointment-card--top { top: 47px; }
  .appointment-card--bottom { top: 607px; }

  .brand { position: absolute; left: 0; top: 0; width: 100%; height: 220px; }
  .brand__mark {
    position: absolute; left: 248px; top: 72px;
    width: 140px; height: 140px; border-radius: 50%;
    background: var(--gold);
  }
  .brand__name {
    position: absolute; left: 412px; top: 112px;
    font-weight: 600; font-size: 44px; line-height: 1; letter-spacing: 1px;
    color: var(--gold); white-space: nowrap;
  }

  .headline {
    position: absolute; left: 0; width: 100%; top: 228px;
    text-align: center; font-size: 35px; font-weight: 400; line-height: 1.2;
  }

  .field {
    position: absolute; top: 300px; width: 250px; height: 31px;
    background: var(--field);
    border-top-right-radius: 30px 31px;
    font-size: 27px; line-height: 31px; padding-left: 8px;
  }
  .field--date { left: 209px; }
  .field--time { left: 483px; padding-left: 5px; }

  .notice {
    position: absolute; left: 242px; top: 372px;
    font-size: 19px; line-height: 23px; font-weight: 400;
  }

  .divider {
    position: absolute; left: 49px; top: 439px; width: 844px; height: 3px;
    background: var(--gold);
  }

  .contact { position: absolute; top: 464px; height: 35px; display: flex; align-items: center; }
  .contact__icon { width: 35px; height: 35px; flex: none; }
  .contact__text { font-size: 17.5px; line-height: 1; white-space: nowrap; margin-left: 12px; }
  .contact--phone { left: 39px; }
  .contact--phone .contact__text { margin-left: 11px; }
  .contact--email { left: 228px; }
  .contact--email .contact__text { margin-left: 6px; }
  .contact--address { left: 524px; }
  .contact--address .contact__text { margin-left: 7px; }
</style>
</head>
<body>

<svg width="0" height="0" style="position:absolute" aria-hidden="true">
  <defs>
    <symbol id="icon-phone" viewBox="0 0 36 36">
      <circle cx="18" cy="18" r="18" fill="#f9b84c"/>
      <path d="M11 9.5c1-1 2.3-.9 3 .2l1.9 3c.6 1 .4 2-.4 2.7l-1.2 1c1 2.4 2.7 4.2 5.1 5.3l1-1.2c.7-.8 1.8-1 2.7-.4l3 1.9c1.1.7 1.2 2 .2 3l-1.5 1.5c-1.3 1.3-3.4 1.5-5.6.4-4.2-2-7.6-5.4-9.6-9.6-1-2.2-.9-4.3.4-5.6z" fill="#231f20"/>
    </symbol>
    <symbol id="icon-mail" viewBox="0 0 36 36">
      <circle cx="18" cy="18" r="18" fill="#f9b84c"/>
      <rect x="8.5" y="11.5" width="19" height="13" rx="2" fill="none" stroke="#231f20" stroke-width="2"/>
      <path d="M9 12.5l9 7 9-7" fill="none" stroke="#231f20" stroke-width="2" stroke-linejoin="round"/>
    </symbol>
    <symbol id="icon-pin" viewBox="0 0 36 36">
      <circle cx="18" cy="18" r="18" fill="#f9b84c"/>
      <path d="M18 7.5c-4 0-7 3-7 6.9 0 5 7 13.6 7 13.6s7-8.6 7-13.6c0-3.9-3-6.9-7-6.9z" fill="#231f20"/>
      <circle cx="18" cy="14.3" r="2.6" fill="#f9b84c"/>
    </symbol>
  </defs>
</svg>

<section class="appointment-card appointment-card--top">
  <div class="brand">
    <span class="brand__mark"></span>
    <span class="brand__name">CORVANTA DENTAL</span>
  </div>
  <h2 class="headline">Your Next Appointment is</h2>
  <div class="field field--date">Date</div>
  <div class="field field--time">Time</div>
  <p class="notice">to cancle or reschedule please notify us at least<br>48hours prior to your scheduled appointment</p>
  <div class="divider"></div>
  <div class="contact contact--phone">
    <svg class="contact__icon"><use href="#icon-phone"/></svg>
    <span class="contact__text">204-555-0172</span>
  </div>
  <div class="contact contact--email">
    <svg class="contact__icon"><use href="#icon-mail"/></svg>
    <span class="contact__text">HELLO@CORVANTAWPG.CA</span>
  </div>
  <div class="contact contact--address">
    <svg class="contact__icon"><use href="#icon-pin"/></svg>
    <span class="contact__text">1480 LARKSPUR HWY , WINNIPEG ,MB</span>
  </div>
</section>

<section class="appointment-card appointment-card--bottom">
  <div class="brand">
    <span class="brand__mark"></span>
    <span class="brand__name">CORVANTA DENTAL</span>
  </div>
  <h2 class="headline">Your Next Appointment is</h2>
  <div class="field field--date">Date</div>
  <div class="field field--time">Time</div>
  <p class="notice">to cancle or reschedule please notify us at least<br>48hours prior to your scheduled appointment</p>
  <div class="divider"></div>
  <div class="contact contact--phone">
    <svg class="contact__icon"><use href="#icon-phone"/></svg>
    <span class="contact__text">204-555-0172</span>
  </div>
  <div class="contact contact--email">
    <svg class="contact__icon"><use href="#icon-mail"/></svg>
    <span class="contact__text">HELLO@CORVANTAWPG.CA</span>
  </div>
  <div class="contact contact--address">
    <svg class="contact__icon"><use href="#icon-pin"/></svg>
    <span class="contact__text">1480 LARKSPUR HWY , WINNIPEG ,MB</span>
  </div>
</section>

</body>
</html>
```